New Website for Consulting Company

Our company needs a fresh web design to help us drive our business forward. We are a consulting and software provider to Airports, Air Traffic Organizations, Builders and Architects. We specialize in analyzing operations, monitoring noise levels and creating software to improve operations, meet customer requirements and improve public relations.
Additional Info:
- Additional requirements can be found in the Web Design Brief
- Logo and logo branding attached
Target Market(s)
Airlines, Airports, Government Agencies, and Real Estate Developers
Industry/Entity Type
Aviation
Coding
Coded - Design and coding required
Number of Pages Required
2 page
Colors
Designer to choose colors to be used in the design.
Requirements
Must have
- - Create a Wordpress Design (Coded - Design and coding required)
- - Designer must provide full implementation/coding depending on the platform chosen by the client (i.e. Wordpress theme, HTML/CSS, etc.)
- - This is a multi-page site; Supporting pages can be formatted the same, but links need to be in place
- - Colors used must be grey scale, black or match the logo. It is not necessary to use all the colors in our logo
Should not have
- We are not looking for an overly bright site. While our logo has 5 different colors, it is not necessary to use all of them.

```html
<!DOCTYPE html>
<html lang="en">
<head>
<meta charset="utf-8">
<title>Skyvane International</title>
<link href="https://fonts.googleapis.com/css2?family=Open+Sans:wght@400;600;700&display=swap" rel="stylesheet">
<style>
:root{
  --purple:#6a5fd6;
  --purple-dark:#3d2fc4;
  --purple-soft:#7d72e0;
  --ink:#333333;
  --muted:#666666;
  --line:#dddddd;
  --btn:#e6e6e6;
  --footer:#f1f1f3;
  --white:#ffffff;
}
*{box-sizing:border-box;margin:0;padding:0}
html,body{width:1200px;height:2528px;overflow:hidden}
body{font-family:"Open Sans",Arial,sans-serif;color:var(--ink);background:var(--white);position:relative;font-size:15px;line-height:1.5}
.abs{position:absolute}

/* hero */
.hero{left:0;top:0;width:1200px;height:480px;background:linear-gradient(180deg,#2f9be6 0%,#8fd0f6 40%,#e8f6fc 62%,#8ccf5a 78%,#4f9a2c 100%)}
.brand{left:30px;top:18px;display:flex;align-items:center;gap:12px;font-size:30px;font-weight:700;color:var(--purple-dark)}
.brand .dot{width:22px;height:22px;background:var(--purple-dark);border-radius:50%}
.nav{right:0;top:0;height:44px;display:flex;background:var(--purple)}
.nav a{color:var(--white);text-decoration:none;font-size:15px;padding:11px 17px}
.nav a.active{background:var(--purple-dark)}

/* solutions */
.section-title{left:0;width:1200px;text-align:center;font-size:30px;font-weight:700;letter-spacing:1px;color:#222}
.solutions-title{top:518px}
.title-rule{left:560px;width:80px;height:2px;background:#222}
.solution{top:600px;width:220px;text-align:center}
.solution .icon{width:80px;height:80px;border-radius:50%;background:var(--purple);margin:0 auto 22px;display:flex;align-items:center;justify-content:center}
.solution h3{font-size:18px;font-weight:600;margin-bottom:8px}
.solution p{font-size:14px;color:var(--muted);line-height:1.45;height:110px}
.btn{display:inline-block;background:var(--btn);border:1px solid #cfcfcf;color:#444;font-size:14px;padding:6px 26px}

/* about */
.about-photo{left:540px;top:1000px;width:660px;height:430px;background:linear-gradient(180deg,#f4f4f6 0%,#dfe1e7 55%,#f7f7f9 100%)}
.about-panel{left:0;top:1000px;width:560px;height:430px;background:var(--purple-soft);color:var(--white);padding:34px 60px 0 120px}
.about-panel h2{font-size:34px;font-weight:600;margin-bottom:10px}
.about-panel p{font-size:14px;line-height:1.5;margin-bottom:24px}
.btn-dark{background:#4a4066;border-color:#4a4066;color:var(--white)}

/* award */
.award-art{left:100px;top:1470px;width:300px;height:330px;background:linear-gradient(180deg,#eef0f6 0%,#c9d2e4 70%,#e9ecf3 100%)}
.award-text{left:488px;top:1500px;width:580px}
.award-text h2{font-size:22px;font-weight:600;margin-bottom:10px}
.award-text p{font-size:14px;color:var(--muted);margin-bottom:26px}
.btn-purple{background:var(--purple);border-color:var(--purple);color:var(--white)}

/* media */
.col-title{font-size:22px;font-weight:600}
.video{left:20px;top:1880px;width:380px;height:240px;background:linear-gradient(135deg,#2b3346 0%,#566a84 60%,#2a3040 100%)}
.video-bar{left:20px;top:2095px;width:380px;height:25px;background:rgba(20,20,30,.85)}
.feed{width:240px}
.feed .item{border-top:1px solid var(--line);padding:10px 0 12px}
.feed h4{font-size:13px;font-weight:700}
.feed p{font-size:12px;color:var(--muted);line-height:1.4}
.feed .date{font-size:11px;color:#999;margin-top:4px}

/* footer */
.footer{left:0;top:2290px;width:1200px;height:238px;background:var(--footer)}
.fcol{top:2318px}
.fcol h5{font-size:14px;font-weight:700;margin-bottom:8px;color:#222}
.fcol li{list-style:none;font-size:12px;color:var(--muted);line-height:1.65}
.contact-line{display:flex;gap:12px;font-size:12px;color:var(--muted);margin-bottom:10px;line-height:1.45}
.footer-brand{left:30px;top:2455px;font-size:22px;font-weight:700;color:var(--purple-dark);display:flex;align-items:center;gap:10px}
.footer-brand .dot{width:16px;height:16px;background:var(--purple-dark);border-radius:50%}
.copyright{left:0;top:2498px;width:1200px;text-align:center;font-size:12px;color:var(--muted)}
</style>
</head>
<body>

<header>
  <div class="abs hero" role="img" aria-label="City skyline beside a runway under a blue sky, green field in front"></div>
  <div class="abs brand"><span class="dot"></span>Skyvane</div>
  <nav class="abs nav">
    <a class="active" href="#">Airports</a><a href="#">Airspace</a><a href="#">Emissions</a><a href="#">Acoustics</a><a href="#">Visualization</a><a href="#">About</a><a href="#">Contact</a>
  </nav>
</header>

<section>
  <h2 class="abs section-title solutions-title">OUR SOLUTIONS</h2>
  <div class="abs title-rule" style="top:566px"></div>

  <div class="abs solution" style="left:120px">
    <div class="icon"><svg width="38" height="38" viewBox="0 0 24 24" fill="#fff"><path d="M21 16v-2l-8-5V3.5a1.5 1.5 0 0 0-3 0V9l-8 5v2l8-2.5V19l-2 1.5V22l3.5-1 3.5 1v-1.5L13 19v-5.5z"/></svg></div>
    <h3>Airports</h3>
    <p>For over 20 years, Skyvane International has been an aviation consulting firm.</p>
    <a class="btn" href="#">Read More</a>
  </div>
  <div class="abs solution" style="left:360px">
    <div class="icon"><svg width="36" height="36" viewBox="0 0 24 24" fill="none" stroke="#fff" stroke-width="2.2" stroke-linecap="round"><path d="M14 6a4 4 0 0 0 5 5l-9 9a2 2 0 0 1-3-3l9-9a4 4 0 0 1-2-2z"/><path d="M4 4l6 6"/></svg></div>
    <h3>Software</h3>
    <p>For over 20 years, Skyvane International has built tools for aviation planning.</p>
    <a class="btn" href="#">Read More</a>
  </div>
  <div class="abs solution" style="left:610px">
    <div class="icon"><svg width="36" height="36" viewBox="0 0 24 24" fill="#fff"><path d="M20 4C9 4 4 9 4 16c0 1.5.3 2.7.8 3.7L4 21h2l.7-1.2C14 20 20 14 20 4z"/></svg></div>
    <h3>Noise &amp; Emissions</h3>
    <p>In our Emissions practice, the team prepares air quality analyses using industry emission and dispersion modeling systems.</p>
    <a class="btn" href="#">Read More</a>
  </div>
  <div class="abs solution" style="left:860px">
    <div class="icon"><svg width="38" height="38" viewBox="0 0 24 24" fill="none" stroke="#fff" stroke-width="2"><path d="M2 12s4-7 10-7 10 7 10 7-4 7-10 7S2 12 2 12z"/><circle cx="12" cy="12" r="3" fill="#fff"/></svg></div>
    <h3>Visualization</h3>
    <p>Skyvane was founded over 10 years ago on the principle that the data has a story to tell.</p>
    <a class="btn" href="#">Read More</a>
  </div>
</section>

<section>
  <div class="abs about-photo" role="img" aria-label="Passenger jet flying low overhead on landing approach"></div>
  <div class="abs about-panel">
    <h2>About</h2>
    <p>Skyvane International is known throughout the aviation industry as a company to turn to when in need of quality, trustworthy noise consulting. Our hard-won reputation over the past 20 years is based in action and is substantiated in our quality interaction with clients as well as the general public. We are proud of our team of airport and acoustic experts.</p>
    <a class="btn btn-dark" href="#">Read More</a>
  </div>
</section>

<section>
  <div class="abs award-art" role="img" aria-label="Glass innovation trophy with an award caption"></div>
  <div class="abs award-text">
    <h2>AEROLYS wins 2012 software innovation!!</h2>
    <p>AEROLYS is a web-based application designed to create, evaluate and display flight operations in 3D. This software tool evaluates the acoustic and environmental impacts from new Performance Based Procedures as well as new runways and airfield configurations, providing a display of noise impacts using various acoustic parameters including A-weighted noise levels and audibility detection.</p>
    <a class="btn btn-purple" href="#">Read More</a>
  </div>
</section>

<section>
  <h3 class="abs col-title" style="left:20px;top:1836px">Video Gallery</h3>
  <div class="abs video" role="img" aria-label="Video player showing a flight track map"></div>
  <div class="abs video-bar"></div>
  <svg class="abs" style="left:28px;top:2100px" width="14" height="16" viewBox="0 0 14 16"><path d="M1 1l12 7-12 7z" fill="#fff"/></svg>

  <h3 class="abs col-title" style="left:540px;top:1836px">News</h3>
  <div class="abs feed" style="left:540px;top:1880px">
    <div class="item"><h4>Passenger Experience</h4><p>Northwind Consulting speaks at a regional airport innovation summit</p><div class="date">19 Jan 2017</div></div>
    <div class="item"><h4>Passenger Experience</h4><p>Northwind Consulting speaks at a regional airport innovation summit</p><div class="date">19 Jan 2017</div></div>
    <div class="item"><h4>Passenger Experience</h4><p>Northwind Consulting speaks at a regional airport innovation summit</p><div class="date">19 Jan 2017</div></div>
  </div>
  <a class="abs btn" style="left:568px;top:2196px" href="#">Read More</a>

  <h3 class="abs col-title" style="left:810px;top:1836px">Events</h3>
  <div class="abs feed" style="left:810px;top:1880px">
    <div class="item"><h4>Passenger Experience</h4><p>Northwind Consulting speaks at a regional airport innovation summit</p><div class="date">19 Jan 2017</div></div>
    <div class="item"><h4>Passenger Experience</h4><p>Northwind Consulting speaks at a regional airport innovation summit</p><div class="date">19 Jan 2017</div></div>
    <div class="item"><h4>Passenger Experience</h4><p>Northwind Consulting speaks at a regional airport innovation summit</p><div class="date">19 Jan 2017</div></div>
  </div>
  <a class="abs btn" style="left:838px;top:2196px" href="#">Read More</a>
</section>

<footer>
  <div class="abs footer"></div>
  <div class="abs fcol" style="left:130px"><h5>SERVICES</h5><ul><li>Airports</li><li>Software</li><li>Noise &amp; Emissions</li><li>Visualization</li></ul></div>
  <div class="abs fcol" style="left:300px"><h5>COMPANY</h5><ul><li>Profile</li><li>Clients</li><li>Experts</li></ul></div>
  <div class="abs fcol" style="left:470px"><h5>INSIGHTS</h5><ul><li>News</li><li>Projects</li><li>Events</li><li>Downloads</li><li>Research</li></ul></div>
  <div class="abs fcol" style="left:640px">
    <h5>CONTACT INFORMATION</h5>
    <div class="contact-line"><svg width="12" height="16" viewBox="0 0 12 16"><path d="M6 0a6 6 0 0 0-6 6c0 4.5 6 10 6 10s6-5.5 6-10a6 6 0 0 0-6-6zm0 8.5A2.5 2.5 0 1 1 6 3.5a2.5 2.5 0 0 1 0 5z" fill="#666"/></svg><span>Skyvane International<br>1450 Harbor View Drive, Suite 310<br>Bayside, California 90000</span></div>
    <div class="contact-line"><svg width="14" height="14" viewBox="0 0 24 24"><path d="M6.6 10.8a15 15 0 0 0 6.6 6.6l2.2-2.2a1 1 0 0 1 1-.25 11.4 11.4 0 0 0 3.6.57 1 1 0 0 1 1 1V20a1 1 0 0 1-1 1A17 17 0 0 1 3 4a1 1 0 0 1 1-1h3.5a1 1 0 0 1 1 1c0 1.25.2 2.45.57 3.57a1 1 0 0 1-.25 1z" fill="#666"/></svg><span>+1 (555) 014-2290</span></div>
    <div class="contact-line"><svg width="14" height="12" viewBox="0 0 14 12"><rect x="0.5" y="0.5" width="13" height="11" fill="none" stroke="#666"/><path d="M0.5 0.5l6.5 6 6.5-6" fill="none" stroke="#666"/></svg><span>hello@skyvane.example</span></div>
  </div>
  <div class="abs footer-brand"><span class="dot"></span>Skyvane</div>
  <div class="abs copyright">©2017 Skyvane International. All rights reserved.</div>
</footer>

</body>
</html>
```